THIS PROJECT IS ONLY ASSIGNED TO MORVANDU

whats up bro!! i just need you to clean my friend design up he do not want anything changed just files and cleaned because it has low resolution

```html
<!DOCTYPE html>
<html lang="en">
<head>
<meta charset="utf-8">
<title>Dorian Vale – Owner / Operator</title>
<link href="https://fonts.googleapis.com/css2?family=PT+Sans+Narrow:wght@700&family=PT+Sans:wght@400;700&family=Titan+One&family=Great+Vibes&display=swap" rel="stylesheet">
<style>
  :root {
    --ink-purple: #4b2a8c;
    --ink-purple-dark: #2e1466;
    --hot-pink: #e64fa6;
    --deep-pink: #9c2377;
    --shadow-grey: #8a8a8a;
    --sky-blue: #4aa6e6;
    --magenta: #d81f7f;
    --script-blue: #4d7ee8;
    --script-violet: #6a2fd0;
    --paper: #ffffff;
  }
  * { margin: 0; padding: 0; box-sizing: border-box; }
  html, body { width: 862px; height: 1200px; overflow: hidden; background: var(--paper); }
  .flyer { position: relative; width: 862px; height: 1200px; overflow: hidden; background: var(--paper); }
  .line {
    position: absolute; left: 0; width: 100%; text-align: center; white-space: nowrap;
  }
  .line-wrap { display: flex; justify-content: center; }
  .stat {
    font-family: "PT Sans Narrow", "PT Sans", sans-serif; font-weight: 700;
    font-size: 47px; line-height: 1; color: var(--ink-purple);
    text-shadow: 1px 1px 0 var(--ink-purple-dark), 2px 2px 1px rgba(46,20,102,.35);
    letter-spacing: -0.2px;
  }
  .headline {
    font-family: "Titan One", sans-serif; font-size: 84px; line-height: 1.1;
    font-weight: 400; white-space: nowrap; padding: 0 12px;
    transform: skewX(-10deg) scale(.76, 1.05); transform-origin: center;
    letter-spacing: -3px;
    background: linear-gradient(180deg, var(--deep-pink) 0%, var(--hot-pink) 100%);
    -webkit-background-clip: text; background-clip: text; color: transparent;
    filter: drop-shadow(-5px -4px 0 var(--shadow-grey)) drop-shadow(1px 1px 0 #c9c9c9);
  }
  .promise { font-size: 45px; }
  .name {
    font-family: "Great Vibes", cursive; font-size: 176px; line-height: 1.2;
    font-weight: 400; padding: 0 50px 20px;
    background: linear-gradient(180deg, var(--script-blue) 20%, var(--script-violet) 85%);
    -webkit-background-clip: text; background-clip: text; color: transparent;
    letter-spacing: -2px;
  }
  .name-rule { position: absolute; left: 110px; top: 826px; width: 728px; height: 4px; }
  .gradient-text {
    font-family: "PT Sans", sans-serif; font-weight: 700; line-height: 1;
    background: linear-gradient(90deg, var(--sky-blue) 0%, var(--sky-blue) 42%, var(--magenta) 58%, var(--magenta) 100%);
    -webkit-background-clip: text; background-clip: text; color: transparent;
  }
  .role { font-family: "PT Sans Narrow", sans-serif; font-size: 50px; }
  .phone { font-size: 100px; letter-spacing: 0; }
  .email { font-family: "PT Sans Narrow", sans-serif; font-size: 53px; letter-spacing: 0.5px; }
</style>
</head>
<body>
<main class="flyer">
  <p class="line stat" style="top:64px;">75% WON’T ANSWER CALLS AFTER PAYMENT</p>
  <p class="line stat" style="top:133px;">65% DON’T COME BACK!</p>
  <p class="line stat" style="top:202px;">OVER 85% HOME OWNER AREN’T HAPPY</p>

  <div class="line line-wrap" style="top:300px;">
    <h1 class="headline">WHY CALL THOSE GUYS?</h1>
  </div>

  <p class="line stat promise" style="top:455px;">WE WILL BE HERE TOMORROW TO</p>
  <p class="line stat promise" style="top:525px;">STAND BEHIND WHAT WE DO</p>
  <p class="line stat promise" style="top:594px;">TODAY</p>

  <div class="line line-wrap" style="top:640px;">
    <h2 class="name">Dorian Vale</h2>
  </div>
  <svg class="name-rule" viewBox="0 0 728 4" preserveAspectRatio="none" aria-hidden="true">
    <defs>
      <linearGradient id="ruleGradient" x1="0" x2="1" y1="0" y2="0">
        <stop offset="0" stop-color="#4aa6e6"/>
        <stop offset="0.45" stop-color="#4aa6e6"/>
        <stop offset="0.62" stop-color="#d81f7f"/>
        <stop offset="1" stop-color="#d81f7f"/>
      </linearGradient>
    </defs>
    <rect x="0" y="0" width="728" height="4" rx="2" fill="url(#ruleGradient)"/>
  </svg>

  <div class="line line-wrap" style="top:880px;">
    <p class="gradient-text role">OWNER / OPERATOR</p>
  </div>
  <div class="line line-wrap" style="top:948px;">
    <p class="gradient-text phone">555-014-2276</p>
  </div>
  <div class="line line-wrap" style="top:1056px;">
    <p class="gradient-text email">NORTHGATESERVICE@MAILBOX.COM</p>
  </div>
</main>
</body>
</html>
```